New company generic tri fold brochure

We are a new small business looking to reach as many potential customers as possible for a low price. We do a variety of self-defense and protection seminars that can be customized to fit the needs of church groups, corporations, community organizations, and families. We do not teach karate, we teach awareness and common self-defense movements that can be instinctively used after just a few hours of training. We believe that self-defense is not only a right, it is your responsibility.

Our preliminary seminar is called Ready for Tomorrow - This is an innovative self-defense and situational awareness personal safety training program. We focus on the predator mindset, tactics and conflict avoidance. We provide seminar attendees with our Easy, Effective, and Practical Personal Protection and life Skills tools to detect, dissuade and defeat a predator. Our goals are to teach everyone to act under extreme stress and respond instinctively using simple, real & practical everyday actions.

Our seminars do not teach “Martial Arts”. We recognize that most people don’t have the time or desire to fully embrace the concepts taught in most karate schools. The skills learned under those controlled situations will more than likely desert us in a crisis. When the body is conditioned, but not the mind, fight or flight will kick in. The bloodstream is flooded with adrenaline, vision and hearing are affected, and the mind fills with a sea of emotions. We simply can’t think normally under those circumstances. We will train you to use techniques instinctively to get you out of dangerous situations.

Everyone has the right to protect themselves and should be able to find a fun, energetic, and educational program that works with their interest, budget and time. Personal and Family protection is not an option….It’s a responsibility. Our martial art science will help you look after yourself and family. 

We also have specialized seminars for women's rape prevention, children's safety and bully handling, weapons training, personal and family protection, and professional defensive & protective procedures.

Our main professor is Carl Hoskins who has almost 40 years of learning and teaching self defense to all ages. We are in the process of setting up our website with more information and seminar dates. When it is ready for public viewing the site name is www.brightguardcourses.net. (GUARD stands for Guided Understanding And Rapid Departure).

I am attaching our main logo and some pictures we have used in the past. We prefer lighter backgrounds and royal blue lettering and accents.

Target Market(s)

Adult men and women ages 18 - 50.

Industry/Entity Type

Education

Font styles to use
Other font styles liked:
• Verdana

Colors
0455a3
ec1f27
ffffff
f04a51
3277b5
33a6d7

Requirements
Must have
• Web address - www.brightguardcourses.net
• Contact Information - Carl Hoskins - ProfessorCarl@brightguardcourses.net (208) 555-0173 and Monica Hoskins - Monica@brightguardcourses.net (208) 555-0186
• Uploaded logo. Brief description of Ready For Tomorrow with emphasis on our ability to customize the seminars to fit any family or group
Should not have
• We are trying to de-emphasize the karate aspect of self-defense. We are NOT a karate school and the seminars we teach do not require any prior knowledge of karate. We use easy to learn, simple, and instinctive moves to avoid confrontations and escape from an attacker.

```html
<!DOCTYPE html>
<html lang="en">
<head>
<meta charset="utf-8">
<title>Bright G.U.A.R.D. Training – Brochure Inside</title>
<link rel="stylesheet" href="https://fonts.googleapis.com/css2?family=Noto+Sans:wght@400&family=Tinos:ital@1&display=swap">
<style>
  :root{
    --royal:#0455a3;
    --sky:#33a6d7;
    --red:#ec1f27;
    --coral:#f04a51;
    --mid-blue:#3277b5;
    --white:#ffffff;
    --mist:#efeff1;
    --ink:#1a1a1a;
  }
  *{margin:0;padding:0;box-sizing:border-box}
  html,body{width:1200px;height:848px;overflow:hidden;background:var(--white)}
  .brochure{position:relative;width:1200px;height:848px;overflow:hidden;font-family:"Noto Sans",Verdana,sans-serif;color:var(--ink)}
  h2,p,blockquote{font-weight:400}
  .panel{position:absolute;top:0;height:848px}
  .panel-learn{left:0;width:400px}
  .panel-skills{left:400px;width:400px}
  .panel-about{left:800px;width:400px;background:var(--mist)}

  .learn-band{position:absolute;left:0;top:0;width:400px;height:65px;background:var(--sky)}
  .learn-band-rule{position:absolute;left:0;top:65px;width:400px;height:12px;background:var(--royal)}
  .learn-title{position:absolute;left:74px;top:30px;color:var(--white);font-size:21px;line-height:28px}

  .photo{position:absolute}
  .photo-family{left:0;top:77px;width:400px;height:284px;background:linear-gradient(135deg,#6d6a66,#c9a58c 55%,#e8a8b4)}
  .photo-range{left:12px;top:87px;width:376px;height:323px;background:linear-gradient(180deg,#9fc6ea 0%,#d6e4f0 38%,#a99a86 42%,#8a7b68 100%)}
  .photo-drill{left:206px;top:633px;width:182px;height:180px;background:linear-gradient(135deg,#e9e9e9,#8a8f98 60%,#3a3d44)}
  .photo-portrait{left:55px;top:100px;width:287px;height:354px;background:linear-gradient(180deg,#7e8a6e,#d8d9dc 45%,#2c2c33 100%)}
  .portrait-rule{position:absolute;left:55px;top:454px;width:287px;height:15px;background:var(--sky)}
  .figure-strip{left:32px;top:622px;width:336px;height:144px;background:linear-gradient(90deg,#1f3550,#c8463a,#1f3550,#c8463a)}

  .body-copy{position:absolute;font-size:15px;line-height:18.75px;white-space:nowrap}
  .learn-copy{left:15px;top:387px}
  .skills-copy{left:12px;top:411px}

  .skills-title{position:absolute;left:15px;top:17px;color:var(--red);font-size:23px;line-height:28px}
  .footer-band{position:absolute;left:0;top:817px;width:800px;height:31px;background:var(--royal)}

  .about-band{position:absolute;left:0;top:0;width:400px;height:344px;background:var(--coral)}
  .about-label{position:absolute;left:23px;top:28px;color:var(--white);font-size:21px;line-height:26px}
  .about-names{position:absolute;left:52px;top:52px;color:var(--white);font-family:"Tinos","Times New Roman",serif;font-style:italic;font-size:33px;line-height:40px;white-space:nowrap}
  .about-quote{position:absolute;left:51px;top:501px;font-size:23px;line-height:27.5px;white-space:nowrap;color:var(--ink)}
  .about-signature{position:absolute;left:83px;top:780px;font-family:"Tinos","Times New Roman",serif;font-style:italic;font-size:30px;line-height:36px;white-space:nowrap}
</style>
</head>
<body>
<div class="brochure">

  <section class="panel panel-learn">
    <div class="learn-band"></div>
    <div class="learn-band-rule"></div>
    <h2 class="learn-title">What you will learn</h2>
    <div class="photo photo-family" role="img" aria-label="Photo of a smiling family gathered around the open back of a packed car"></div>
    <p class="body-copy learn-copy">Our preliminary seminar is called Ready for<br>Tomorrow - This is an innovative self-defense and<br>situational awareness personal safety training<br>program. We focus on the predator mindset,<br>tactics and conflict avoidance. We provide<br>seminar attendees with our Easy, Effective,<br>and Practical Personal Protection and life Skills<br>tools to detect, dissuade and defeat a predator.<br>Our goals are to teach everyone to act under<br>extreme stress and respond instinctively using<br>simple, real &amp; practical everyday actions.</p>
    <div class="photo figure-strip" role="img" aria-label="Illustration of blue and red figures demonstrating self-defense moves"></div>
  </section>

  <section class="panel panel-skills">
    <h2 class="skills-title">Easy, Effective, &amp; Practical<br>Personal Protection &amp; Life Skills</h2>
    <div class="photo photo-range" role="img" aria-label="Photo of an instructor coaching a student at an outdoor firing range"></div>
    <p class="body-copy skills-copy">Our seminars do not teach “Martial Arts”. We<br>recognize that most people don’t have the time<br>or desire to fully embrace the concepts taught<br>in most karate schools. The skills learned<br>under those controlled situations will more than<br>likely desert us in a crisis. When the body is<br>conditioned, but not the mind, fight or flight<br>will kick in. The bloodstream is flooded with<br>adrenaline, vision and hearing are affected,<br>and the mind fills with a sea of emotions. We<br>simply can’t think normally under those<br>circumstances. We will<br>train you to use<br>techniques instinctively<br>to get you out of<br>dangerous situations.</p>
    <div class="photo photo-drill" role="img" aria-label="Photo of a woman practising a self-defense strike with an instructor"></div>
  </section>

  <div class="footer-band"></div>

  <section class="panel panel-about">
    <div class="about-band"></div>
    <h2 class="about-label">About</h2>
    <p class="about-names">Carl &amp; Monica Hoskins</p>
    <div class="photo photo-portrait" role="img" aria-label="Portrait photo of the lead instructor in a suit standing by a white car"></div>
    <div class="portrait-rule"></div>
    <blockquote class="about-quote">“My wife, Monica, and I<br>established Bright G.U.A.R.D.<br>Training as a positive way<br>to use my 39 years of<br>Martial Arts, personal<br>protection training and<br>knowledge to reach as<br>many people both casual<br>and professional, as<br>possible.”</blockquote>
    <p class="about-signature">- Professor Carl Hoskins</p>
  </section>

</div>
</body>
</html>
```